'Tarnby Electrical' web design

I need a web design for an electrical/electrician company based in sydney called tarnby electrical. The logo design and business card design have been uploaded to be used on the web design. I want the design to be very modern and clean. I want the sector designs on the business card, i.e "residential", "commercial" etc, to be fleshed out on the front page. Base those sector designs off the business card but try to make them more minimal and modern to suit the website. Contact details are also on the business card. Try to suit the colour scheme of the logo. The sector designs should be up the top and linked so when clicked it will scroll down the website to brief descriptions of the work the company does in those sectors. I want the website to mainly attract builders, insurance companies and the commercial sector. I want the website to look unique. Custom graphics would be nice to make the website standout. I don't want the website to look like generic.

Target Market(s)

Builders, commercial sector, home owners

Industry/Entity Type

Electrical/Construction

Coding

Coded - Design and coding required

Number of Pages Required

3 page

Requirements
Must have
• Modern design
Nice to have
• Custom graphics that make the website unique

```html
<!DOCTYPE html>
<html lang="en">
<head>
<meta charset="utf-8">
<title>Tarnby Electrical</title>
<link href="https://fonts.googleapis.com/css2?family=Montserrat:wght@500;600;700;800;900&family=Open+Sans:wght@400;600&display=swap" rel="stylesheet">
<style>
:root{
  --navy:#1c1a4d;
  --navy-deep:#15133b;
  --purple:#3b2a6b;
  --plum:#6a4a86;
  --orange:#f7931e;
  --coral:#e86a4a;
  --yellow:#ffc20e;
  --teal:#2f8f9d;
  --sky:#9ec9e6;
  --blue-pale:#eaf2fb;
  --ring:#dbe7f7;
  --text:#3a3a4a;
  --white:#ffffff;
}
*{margin:0;padding:0;box-sizing:border-box}
html,body{width:1200px;height:4272px;overflow:hidden}
body{position:relative;background:var(--white);font-family:'Open Sans',Arial,sans-serif;color:var(--text)}
.abs{position:absolute}
.btn{display:inline-block;background:var(--yellow);color:var(--navy);font-family:'Montserrat',Arial,sans-serif;font-weight:700;font-size:14px;padding:11px 28px;border-radius:24px;text-decoration:none}
.brand{font-family:'Montserrat',Arial,sans-serif;font-weight:800;color:var(--white);letter-spacing:1px;display:flex;align-items:center;gap:12px;white-space:nowrap}
.brand .mark{background:var(--orange);display:inline-block;flex:none}

/* hero */
.hero{left:0;top:0;width:1200px;height:690px;background:linear-gradient(180deg,var(--navy-deep) 0%,#2a2160 45%,#4a3476 80%,#6a4a86 100%);border-radius:0 0 50% 50% / 0 0 110px 110px;overflow:hidden}
.hero-art{left:430px;top:40px;width:770px;height:600px;background:radial-gradient(ellipse 60% 55% at 62% 55%,rgba(247,147,30,.35) 0%,rgba(120,160,220,.35) 35%,rgba(59,42,107,0) 75%),radial-gradient(ellipse 40% 30% at 78% 78%,rgba(58,110,190,.55),rgba(58,110,190,0) 80%)}
.topbar{left:0;top:0;width:1200px;height:64px;display:flex;align-items:center;justify-content:space-between;padding:0 60px}
.topbar .brand{font-size:20px}
.topbar .brand .mark{width:18px;height:18px}
.topbar .right{display:flex;align-items:center;gap:28px}
.phone-pill{background:var(--yellow);color:var(--navy);font-family:'Montserrat',Arial,sans-serif;font-weight:700;font-size:14px;padding:8px 18px;border-radius:20px;display:flex;align-items:center;gap:8px}
.burger{width:26px;height:18px;display:flex;flex-direction:column;justify-content:space-between}
.burger span{height:3px;background:var(--white);border-radius:2px}
.hero-copy{left:60px;top:225px}
.hero-copy .brand{font-size:52px}
.hero-copy .brand .mark{width:44px;height:44px}
.tagline{font-family:'Montserrat',Arial,sans-serif;font-weight:600;color:var(--white);letter-spacing:6px;font-size:15px;margin:14px 0 36px}

/* sectors */
.sectors{left:0;top:575px;width:1200px}
.sector{position:absolute;width:210px;text-align:center;text-decoration:none}
.sector .disc{margin:0 auto;width:200px;height:200px;border-radius:50%;background:var(--white);border:7px solid var(--navy);display:flex;align-items:center;justify-content:center;box-shadow:0 8px 24px rgba(20,18,58,.18)}
.sector .art{width:120px;height:120px;border-radius:18px}
.sector .label{display:block;margin-top:40px;font-family:'Montserrat',Arial,sans-serif;font-weight:800;font-size:17px;color:var(--navy);letter-spacing:.5px}
.sector.active .label{color:var(--orange)}
.sector.active .disc{border-color:var(--orange)}
.sector.active:after{content:"";position:absolute;left:0;right:0;top:278px;height:4px;background:var(--yellow);border-radius:2px}

.section-title{left:0;top:920px;width:1200px;text-align:center;font-family:'Montserrat',Arial,sans-serif;font-weight:900;font-size:40px;color:var(--navy)}
.section-title em{font-style:normal;color:var(--orange)}

/* services */
.band{left:0;width:1200px;background:var(--blue-pale)}
.service-art{width:440px;height:440px;border-radius:50%;border:12px solid var(--ring);box-shadow:0 10px 30px rgba(20,18,58,.12)}
.service-copy{width:500px}
.service-copy h2{font-family:'Montserrat',Arial,sans-serif;font-weight:800;font-size:32px;color:var(--navy);margin-bottom:8px;letter-spacing:.5px}
.service-copy p{font-size:14px;line-height:1.5;margin-bottom:12px}
.service-copy .btn{margin-top:8px}

/* cta */
.cta-art{left:0;top:3520px;width:1200px;height:440px;background:linear-gradient(90deg,#f4a27a 0%,#f6c5b3 12%,rgba(255,255,255,0) 24%,rgba(255,255,255,0) 76%,#f6c5b3 88%,#f4a27a 100%),linear-gradient(180deg,#ffffff 0%,#eef1f7 55%,#f0b08a 85%,#e8604a 100%)}
.cta{left:0;top:3400px;width:1200px;text-align:center}
.cta h2{font-family:'Montserrat',Arial,sans-serif;font-weight:900;font-size:40px;line-height:1.2;color:var(--navy);width:820px;margin:0 auto}
.cta h2 em{font-style:normal;color:var(--orange)}
.cta p{width:620px;margin:14px auto 22px;font-size:14px;line-height:1.5}

/* footer */
.footer{left:0;top:3960px;width:1200px;height:312px;background:var(--navy)}
.footer .brand{position:absolute;left:0;right:0;top:50px;justify-content:center;font-size:32px}
.footer .brand .mark{width:28px;height:28px}
.contacts{position:absolute;left:0;top:128px;width:1200px;display:flex;justify-content:center;gap:120px}
.contact{width:200px;text-align:center;color:var(--white);font-size:13px;line-height:1.5}
.contact .ico{width:48px;height:48px;border:2px solid var(--white);border-radius:50%;margin:0 auto 14px;display:flex;align-items:center;justify-content:center}
.copyright{position:absolute;left:0;right:0;bottom:18px;text-align:center;color:#c9c8df;font-size:12px}
.copyright strong{color:var(--white)}
</style>
</head>
<body>

<div class="abs hero">
  <div class="abs hero-art" role="img" aria-label="Illustration of electricians working on power poles and solar panels beside transmission towers"></div>
</div>

<header class="abs topbar">
  <div class="brand"><span class="mark"></span>TARNBY ELECTRICAL</div>
  <div class="right">
    <div class="phone-pill">
      <svg width="14" height="14" viewBox="0 0 24 24"><path fill="#1c1a4d" d="M6.6 10.8a15 15 0 006.6 6.6l2.2-2.2a1 1 0 011-.25 11.4 11.4 0 003.6.57 1 1 0 011 1V20a1 1 0 01-1 1A17 17 0 013 4a1 1 0 011-1h3.5a1 1 0 011 1c0 1.25.2 2.45.57 3.57a1 1 0 01-.25 1z"/></svg>
      +0400 123 456
    </div>
    <div class="burger"><span></span><span></span><span></span></div>
  </div>
</header>

<div class="abs hero-copy">
  <div class="brand"><span class="mark"></span>TARNBY ELECTRICAL</div>
  <div class="tagline">POWERING YOUR PROJECTS</div>
  <a class="btn" href="#contact">Get A Free Quote</a>
</div>

<nav class="abs sectors">
  <a class="sector active" href="#commercial" style="left:85px;top:0"><span class="disc"><span class="art" style="background:linear-gradient(180deg,#f7931e 0%,#f3b04a 45%,#3b2a6b 100%)" role="img" aria-label="Commercial shopfront icon"></span></span><span class="label">COMMERCIAL</span></a>
  <a class="sector" href="#construction" style="left:345px;top:0"><span class="disc"><span class="art" style="border-radius:50%;background:linear-gradient(180deg,#ffc20e 0%,#f29a4a 45%,#3a5aa0 100%)" role="img" aria-label="Construction worker icon"></span></span><span class="label">CONSTRUCTION</span></a>
  <a class="sector" href="#industrial" style="left:620px;top:0"><span class="disc"><span class="art" style="background:linear-gradient(180deg,#9aa6c4 0%,#e8604a 50%,#1c1a4d 100%)" role="img" aria-label="Industrial factory icon"></span></span><span class="label">INDUSTRIAL</span></a>
  <a class="sector" href="#residential" style="left:900px;top:0"><span class="disc"><span class="art" style="background:linear-gradient(180deg,#c0392b 0%,#f7931e 45%,#f3d6a4 100%)" role="img" aria-label="Residential house icon"></span></span><span class="label">RESIDENTIAL</span></a>
</nav>

<h1 class="abs section-title">WHAT <em>WE</em> DO</h1>

<!-- Residential -->
<div class="abs service-art" id="residential" style="left:75px;top:1020px;background:radial-gradient(circle at 50% 38%,#e9dcc8 0%,#b9c9dc 30%,#5a6aa0 60%,#2c2a5e 100%)" role="img" aria-label="Illustration of a modern two-storey home"></div>
<div class="abs service-copy" style="left:628px;top:1070px">
  <h2>RESIDENTIAL</h2>
  <p>Lorem Ipsum is simply dummy text of the printing and typesetting industry. Lorem Ipsum has been the industry's standard dummy text ever since the 1500s, when an unknown printer took a galley of type and scrambled it to make a type specimen book. It has survived not only five centuries, but also the leap into electronic typesetting, remaining essentially unchanged. It was popularised in the 1960s with the release of Letraset sheets containing.</p>
  <p>Lorem Ipsum passages, and more recently with desktop publishing software like Aldus PageMaker including versions of Lorem Ipsum.</p>
  <a class="btn" href="#contact">Learn More</a>
</div>

<!-- Commercial -->
<div class="abs band" style="top:1548px;height:572px"></div>
<div class="abs service-copy" id="commercial" style="left:60px;top:1690px">
  <h2>COMMERCIAL</h2>
  <p>Lorem Ipsum is simply dummy text of the printing and typesetting industry. Lorem Ipsum has been the industry's standard dummy text ever since the 1500s, when an unknown printer took a galley of type and scrambled it to make a type specimen book. It has survived not only five centuries, but also the leap into electronic typesetting, remaining essentially unchanged. It was popularised in the 1960s with the release of Letraset sheets containing.</p>
  <p>Lorem Ipsum passages, and more recently with desktop publishing software like Aldus PageMaker including versions of Lorem Ipsum.</p>
  <a class="btn" href="#contact">Learn More</a>
</div>
<div class="abs service-art" style="left:660px;top:1610px;background:linear-gradient(180deg,#3a2f6e 0%,#6a4a86 25%,#e86a4a 55%,#f3a36a 75%,#2c3a5e 100%)" role="img" aria-label="Illustration of city office towers"></div>

<!-- Industrial -->
<div class="abs service-art" id="industrial" style="left:75px;top:2210px;background:linear-gradient(180deg,#2e2760 0%,#5a4a8a 30%,#e8604a 48%,#2f8f9d 68%,#e5873a 100%)" role="img" aria-label="Illustration of an industrial plant with chimneys"></div>
<div class="abs service-copy" style="left:628px;top:2265px">
  <h2>INDUSTRIAL</h2>
  <p>Lorem Ipsum is simply dummy text of the printing and typesetting industry. Lorem Ipsum has been the industry's standard dummy text ever since the 1500s, when an unknown printer took a galley of type and scrambled it to make a type specimen book. It has survived not only five centuries, but also the leap into electronic typesetting, remaining essentially unchanged. It was popularised in the 1960s with the release of Letraset sheets containing.</p>
  <p>Lorem Ipsum passages, and more recently with desktop publishing software like Aldus PageMaker including versions of Lorem Ipsum.</p>
  <a class="btn" href="#contact">Learn More</a>
</div>

<!-- Construction -->
<div class="abs band" style="top:2760px;height:560px"></div>
<div class="abs service-copy" id="construction" style="left:60px;top:2870px">
  <h2>CONSTRUCTION</h2>
  <p>Lorem Ipsum is simply dummy text of the printing and typesetting industry. Lorem Ipsum has been the industry's standard dummy text ever since the 1500s, when an unknown printer took a galley of type and scrambled it to make a type specimen book. It has survived not only five centuries, but also the leap into electronic typesetting, remaining essentially unchanged. It was popularised in the 1960s with the release of Letraset sheets containing.</p>
  <p>Lorem Ipsum passages, and more recently with desktop publishing software like Aldus PageMaker including versions of Lorem Ipsum.</p>
  <a class="btn" href="#contact">Learn More</a>
</div>
<div class="abs service-art" style="left:660px;top:2810px;background:linear-gradient(180deg,#2c2560 0%,#6a4a86 30%,#f3b04a 50%,#9aa4b6 70%,#4a4e68 100%)" role="img" aria-label="Illustration of a building under construction with a crane"></div>

<!-- CTA -->
<div class="abs cta-art" role="img" aria-label="Illustration of power pylons, chimneys and an industrial skyline"></div>
<section class="abs cta" id="contact">
  <h2>Lorem Ipsum is simply dummy text of the printing <em>and typesetting industry.</em></h2>
  <p>Lorem Ipsum is simply dummy text of the printing and typesetting industry. Lorem Ipsum has been the industry's standard dummy text ever since the 1500s, when an unknown printer.</p>
  <a class="btn" href="#contact">Get A Free Quote</a>
</section>

<!-- Footer -->
<footer class="abs footer">
  <div class="brand"><span class="mark"></span>TARNBY ELECTRICAL</div>
  <div class="contacts">
    <div class="contact">
      <div class="ico"><svg width="20" height="20" viewBox="0 0 24 24"><path fill="#fff" d="M12 2a7 7 0 00-7 7c0 5 7 13 7 13s7-8 7-13a7 7 0 00-7-7zm0 9.5A2.5 2.5 0 1112 6.5a2.5 2.5 0 010 5z"/></svg></div>
      123, Lorem Ipsum is a dummy text
    </div>
    <div class="contact">
      <div class="ico"><svg width="20" height="20" viewBox="0 0 24 24"><path fill="#fff" d="M6.6 10.8a15 15 0 006.6 6.6l2.2-2.2a1 1 0 011-.25 11.4 11.4 0 003.6.57 1 1 0 011 1V20a1 1 0 01-1 1A17 17 0 013 4a1 1 0 011-1h3.5a1 1 0 011 1c0 1.25.2 2.45.57 3.57a1 1 0 01-.25 1z"/></svg></div>
      +0400 123 456
    </div>
    <div class="contact">
      <div class="ico"><svg width="20" height="20" viewBox="0 0 24 24"><path fill="none" stroke="#fff" stroke-width="2" d="M3 6h18v12H3z M3 6l9 7 9-7"/></svg></div>
      hello@tarnbyelectrical.com
    </div>
  </div>
  <div class="copyright">© Copyright 2023 <strong>TARNBY ELECTRICAL</strong> All Right Reserved</div>
</footer>

</body>
</html>
```